Business card for apparel company. Specializing in fishing and boating performance wear. Main company name is Marlowe Teal Company, LLC brand name for apparel is WAKEFIN. See website www.WakefinReefline.com I will attach some logos to consider.

```html
<!DOCTYPE html>
<html lang="en">
<head>
<meta charset="utf-8">
<title>Wakefin Business Card</title>
<link rel="stylesheet" href="https://fonts.googleapis.com/css2?family=Montserrat:wght@400;700;800&display=swap">
<style>
  :root {
    --backdrop: #7d6a52;
    --card-white: #ffffff;
    --brand-blue: #2a8ad8;
    --name-blue: #2b8fd3;
    --rule-blue: #3a87c7;
    --text-dark: #333a40;
    --text-muted: #4a4f55;
    --back-light: #30a2e2;
    --back-dark: #2a76c4;
    --watermark: #f1f5fa;
  }
  * { margin: 0; padding: 0; box-sizing: border-box; }
  html, body { width: 900px; height: 1200px; overflow: hidden; }
  body {
    position: relative;
    background: var(--backdrop);
    font-family: "Montserrat", Arial, sans-serif;
  }
  .card {
    position: absolute;
    left: 80px;
    width: 742px;
    height: 440px;
    border-radius: 30px;
    overflow: hidden;
  }
  .card-front { top: 132px; background: var(--card-white); }
  .card-back {
    top: 638px;
    background: linear-gradient(135deg, var(--back-light), var(--back-dark));
  }
  .front-watermark {
    position: absolute;
    left: 300px; top: 20px;
    width: 442px; height: 250px;
    background: radial-gradient(ellipse at 60% 50%, var(--watermark), rgba(255,255,255,0) 70%);
  }
  .brand-name {
    position: absolute;
    left: 42px; top: 160px;
    font-size: 48px;
    font-weight: 800;
    letter-spacing: 1px;
    color: var(--brand-blue);
    line-height: 1;
  }
  .person-name {
    position: absolute;
    left: 42px; top: 267px;
    font-size: 26px;
    font-weight: 700;
    color: var(--name-blue);
    line-height: 1;
  }
  .person-role {
    position: absolute;
    left: 42px; top: 299px;
    font-size: 16px;
    color: var(--text-muted);
    line-height: 1;
  }
  .divider {
    position: absolute;
    left: 42px; top: 328px;
    width: 670px; height: 1.5px;
    background: var(--rule-blue);
  }
  .contact-list {
    position: absolute;
    left: 42px; top: 347px;
    list-style: none;
    font-size: 16px;
    color: var(--text-dark);
  }
  .contact-list li {
    display: flex;
    align-items: center;
    height: 22px;
  }
  .contact-list svg { width: 14px; height: 14px; margin-right: 12px; fill: var(--rule-blue); }
  .company-address {
    position: absolute;
    left: 448px; top: 347px;
    font-style: normal;
    font-size: 16px;
    line-height: 19.5px;
    color: var(--text-dark);
  }
  .back-pattern {
    position: absolute;
    inset: 0;
    background: repeating-linear-gradient(0deg, rgba(255,255,255,0.06) 0 34px, rgba(255,255,255,0) 34px 72px);
  }
  .back-brand {
    position: absolute;
    left: 520px; top: 296px;
    font-size: 28px;
    font-weight: 800;
    color: var(--card-white);
    line-height: 1;
  }
</style>
</head>
<body>
  <section class="card card-front">
    <div class="front-watermark" role="img" aria-label="Faint oversized brand mark decoration"></div>
    <div class="brand-name">WAKEFIN</div>
    <h1 class="person-name">Corin Abernathy</h1>
    <p class="person-role">Owner</p>
    <div class="divider"></div>
    <ul class="contact-list">
      <li><svg viewBox="0 0 24 24"><path d="M6.6 10.8a15.1 15.1 0 0 0 6.6 6.6l2.2-2.2a1 1 0 0 1 1-.25 11.4 11.4 0 0 0 3.6.57 1 1 0 0 1 1 1V20a1 1 0 0 1-1 1A17 17 0 0 1 3 4a1 1 0 0 1 1-1h3.5a1 1 0 0 1 1 1c0 1.25.2 2.45.57 3.6a1 1 0 0 1-.25 1z"/></svg>727-555-0142</li>
      <li><svg viewBox="0 0 24 24"><path d="M2 5h20v14H2z M2 5l10 8 10-8" /><path d="M3 6.5l9 7 9-7V18H3z" fill="#fff" opacity="0.25"/></svg>info@MarloweTealCo.com</li>
      <li><svg viewBox="0 0 24 24"><path d="M12 2a10 10 0 1 0 0 20 10 10 0 0 0 0-20zm0 2c1.2 1.4 2 3.6 2.3 6H9.7C10 7.6 10.8 5.4 12 4zm-2.3 8h4.6c-.3 2.4-1.1 4.6-2.3 6-1.2-1.4-2-3.6-2.3-6z"/></svg>www.WakefinReefline.com</li>
    </ul>
    <address class="company-address">
      Marlowe Teal Company, LLC<br>
      P.O. Box 418<br>
      Seabright, Florida 34611
    </address>
  </section>

  <section class="card card-back">
    <div class="back-pattern" role="img" aria-label="Repeating pattern of the brand mark in lighter blue"></div>
    <div class="back-brand">WAKEFIN</div>
  </section>
</body>
</html>
```